Falcrest security business card

Looking for a business card for my security company

Target Market(s)

Security

Industry/Entity Type

Security

Contact Information for Business Card

Name - Gil Marston. Title - General manager - direct 314 862.4490 website www. falcrestsecurityservices.example email - gil@ falcrestsecurityservices.example

Requirements
Must have
• Logo attached

```html
<!DOCTYPE html>
<html lang="en">
<head>
<meta charset="utf-8">
<title>Falcrest Security Services – Business Card</title>
<link rel="stylesheet" href="https://fonts.googleapis.com/css2?family=Montserrat:wght@400;500;600&display=swap">
<style>
  :root {
    --page-bg: #ececec;
    --card-bg: #050608;
    --gold: #c9a063;
    --gold-light: #e2c58f;
    --ink-light: #f2f2f2;
  }
  * { margin: 0; padding: 0; box-sizing: border-box; }
  html, body {
    width: 1200px;
    height: 1164px;
    overflow: hidden;
    background: var(--page-bg);
    font-family: "Montserrat", Arial, sans-serif;
  }
  .sheet {
    width: 1200px;
    height: 1164px;
    display: flex;
    flex-direction: column;
    align-items: center;
    justify-content: center;
    gap: 28px;
  }
  .card {
    position: relative;
    width: 900px;
    height: 540px;
    background: var(--card-bg);
    color: var(--ink-light);
  }
  .card-front .person {
    position: absolute;
    left: 65px;
    top: 90px;
  }
  .person-name {
    font-size: 31px;
    font-weight: 500;
    color: var(--gold);
    letter-spacing: 0.3px;
  }
  .person-title {
    margin-top: 4px;
    font-size: 20px;
    font-weight: 500;
  }
  .wordmark {
    position: absolute;
    font-weight: 600;
    color: var(--gold);
    text-transform: uppercase;
    letter-spacing: 1px;
    display: flex;
    align-items: center;
    gap: 12px;
    white-space: nowrap;
  }
  .wordmark-dot {
    width: 14px;
    height: 14px;
    border-radius: 50%;
    background: var(--gold);
  }
  .card-front .wordmark {
    font-size: 52px;
    left: 540px;
    top: 215px;
    transform: translateX(-50%);
  }
  .card-back .wordmark {
    font-size: 78px;
    left: 50%;
    top: 50%;
    transform: translate(-50%, -50%);
  }
  .contact-list {
    position: absolute;
    left: 65px;
    top: 365px;
    list-style: none;
  }
  .contact-item {
    display: flex;
    align-items: center;
    gap: 12px;
    font-size: 22px;
    font-weight: 400;
    line-height: 1;
  }
  .contact-item + .contact-item { margin-top: 14px; }
  .contact-item:first-child { margin-bottom: 14px; }
  .contact-icon {
    width: 20px;
    height: 20px;
    flex: none;
  }
</style>
</head>
<body>
<main class="sheet">
  <section class="card card-front" aria-label="Business card front">
    <div class="person">
      <p class="person-name">Gil Marston</p>
      <p class="person-title">General Manager</p>
    </div>

    <div class="wordmark"><span class="wordmark-dot"></span>Falcrest</div>

    <ul class="contact-list">
      <li class="contact-item">
        <svg class="contact-icon" viewBox="0 0 20 20" aria-hidden="true">
          <path d="M5 2.5l3 3.2-1.8 2a10 10 0 0 0 6.1 6.1l2-1.8 3.2 3-1.8 2.4C9.5 17.4 2.6 10.5 2.6 4.3z" fill="var(--gold)"/>
        </svg>
        314 862.4490
      </li>
      <li class="contact-item">
        <svg class="contact-icon" viewBox="0 0 20 20" aria-hidden="true">
          <rect x="2" y="5" width="16" height="11" fill="var(--gold)"/>
          <path d="M2 5l8 6 8-6" fill="none" stroke="var(--card-bg)" stroke-width="1.4"/>
        </svg>
        gil@falcrestsecurityservices.example
      </li>
      <li class="contact-item">
        <svg class="contact-icon" viewBox="0 0 20 20" aria-hidden="true">
          <g fill="none" stroke="var(--gold)" stroke-width="1.4">
            <circle cx="10" cy="10" r="8"/>
            <ellipse cx="10" cy="10" rx="3.5" ry="8"/>
            <path d="M2 10h16M3.5 6h13M3.5 14h13"/>
          </g>
        </svg>
        falcrestsecurityservices.example
      </li>
    </ul>
  </section>

  <section class="card card-back" aria-label="Business card back">
    <div class="wordmark"><span class="wordmark-dot"></span>Falcrest</div>
  </section>
</main>
</body>
</html>
```